Banner for back of trucks

We make a product that is called "Brindo".
It attaches to the side of hay balers and automatically applies tags to bales as they are being made.
We require a simple / modern banner design that will be affixed to the back of hay trucks showing that the hay on board has been Marked by Brindo.
The banner will be 52x91cm (landscape)
The banner needs to say "Marked by Brindo" using the company logo.
It also needs the website "www.brindo.com.au" displayed.
We have attached an image of our logo, the product itself and the back of a truck it will be attached to for reference.

```html
<!DOCTYPE html>
<html lang="en">
<head>
<meta charset="utf-8">
<title>Marked by Brindo – Truck Banner</title>
<link rel="stylesheet" href="https://fonts.googleapis.com/css2?family=Tinos:ital,wght@0,400;1,400&display=swap">
<style>
  :root {
    --brand-orange: #f9ad1c;
    --brand-grey: #6b6760;
    --paper: #ffffff;
    --serif: "Tinos", "Times New Roman", serif;
  }
  html, body {
    margin: 0;
    padding: 0;
    width: 1200px;
    height: 686px;
    overflow: hidden;
    background: var(--paper);
  }
  .banner {
    width: 1200px;
    height: 686px;
    display: flex;
    flex-direction: column;
    font-family: var(--serif);
  }
  .banner__headline-band {
    height: 278px;
    background: var(--brand-orange);
    display: flex;
    align-items: center;
    justify-content: center;
  }
  .headline {
    margin: 0;
    color: var(--paper);
    font-style: italic;
    font-weight: 400;
    font-size: 250px;
    line-height: 1;
    letter-spacing: -4px;
    transform: translateY(14px);
  }
  .banner__brand-band {
    height: 274px;
    background: var(--paper);
    display: flex;
    align-items: baseline;
    justify-content: center;
    gap: 26px;
    box-sizing: border-box;
    padding-top: 36px;
  }
  .brand-by {
    color: var(--brand-grey);
    font-style: italic;
    font-size: 200px;
    line-height: 1;
  }
  .brand-name {
    color: var(--brand-grey);
    font-style: normal;
    font-weight: 400;
    font-size: 196px;
    line-height: 1;
  }
  .banner__web-band {
    height: 134px;
    background: var(--brand-grey);
    display: flex;
    align-items: center;
    justify-content: center;
  }
  .web-address {
    color: var(--paper);
    font-style: italic;
    font-size: 94px;
    line-height: 1;
    transform: translateY(-4px);
  }
</style>
</head>
<body>
  <main class="banner">
    <section class="banner__headline-band">
      <h1 class="headline">MARKED</h1>
    </section>
    <section class="banner__brand-band">
      <span class="brand-by">by</span>
      <span class="brand-name">Brindo</span>
    </section>
    <section class="banner__web-band">
      <span class="web-address">www.brindo.com.au</span>
    </section>
  </main>
</body>
</html>
```